Business card design for Plumbing and Gas fitting company

We need a business card design for our plumbing and gas fitting company using the company logo and director details. Design should be modern and eye-catching however kept reasonably simple. This design should be targeted at commercial businesses/work so professionalism is key.

Target Market(s)

Commercial/business

Industry/Entity Type

Plumbing

Contact Information for Business Card

Warwick Tane
Director
027 815 0937
warwick@harbourlinepipeworks.example
PO Box 8716
Palmerston North 4441

Font styles to use
Sans Serif

Requirements
Must have
• Logo
• Modern
• Kept simple
Nice to have
• Colour scheme based around logo

```html
<!DOCTYPE html>
<html lang="en">
<head>
<meta charset="utf-8">
<title>Harbourline Pipeworks – Business Card</title>
<link href="https://fonts.googleapis.com/css2?family=Josefin+Sans:wght@300;400;600;700&display=swap" rel="stylesheet">
<style>
  :root {
    --backdrop: #e8e3de;
    --card: #171717;
    --orange: #e8772e;
    --blue: #1a74c4;
    --grey: #8a8a8a;
    --white: #f4f4f4;
    --muted: #a8a8a8;
    --rule: #5a5a5a;
  }
  * { box-sizing: border-box; margin: 0; padding: 0; }
  html, body {
    width: 1200px; height: 799px; overflow: hidden;
    background: var(--backdrop);
    font-family: "Josefin Sans", sans-serif;
  }
  .canvas { position: relative; width: 1200px; height: 799px; }

  .card {
    position: absolute; top: 283px;
    width: 445px; height: 248px;
    background: var(--card);
    box-shadow: 0 3px 10px rgba(0,0,0,0.25);
    overflow: hidden;
  }
  .card--front { left: 139px; }
  .card--back { left: 624px; }

  .card__stripe { position: absolute; left: 0; top: 0; height: 100%; }
  .card--front .card__stripe { width: 39px; background: var(--orange); }
  .card--back .card__stripe { width: 28px; background: var(--blue); }
  .card__notch {
    position: absolute; top: 116px; width: 0; height: 0;
    border-top: 8px solid transparent; border-bottom: 8px solid transparent;
  }
  .card--front .card__notch { left: 39px; border-left: 8px solid var(--orange); }
  .card--back .card__notch { left: 28px; border-left: 8px solid var(--blue); }

  .brand {
    position: absolute; display: flex; align-items: center;
    color: var(--grey); font-weight: 700; white-space: nowrap;
  }
  .brand__name { display: block; }
  .brand__dot { border-radius: 50%; background: var(--orange); flex: none; }
  .card--front .brand { left: 75px; top: 92px; font-size: 30px; line-height: 32px; gap: 12px; }
  .card--front .brand__dot { width: 26px; height: 26px; }
  .card--back .brand { left: 50px; top: 104px; font-size: 15px; line-height: 16px; gap: 6px; }
  .card--back .brand__dot { width: 12px; height: 12px; }

  .divider {
    position: absolute; left: 194px; top: 47px;
    width: 1px; height: 165px; background: var(--rule);
  }

  .contact { position: absolute; left: 216px; top: 50px; }
  .contact__name {
    color: var(--white); font-weight: 600; font-size: 17px;
    letter-spacing: 1.5px; text-transform: uppercase;
  }
  .contact__role {
    color: var(--muted); font-size: 8px; font-weight: 300;
    letter-spacing: 1px; text-transform: uppercase; margin-top: 4px;
  }
  .contact__list { list-style: none; margin-top: 40px; }
  .contact__item {
    display: flex; align-items: flex-start; gap: 7px;
    color: var(--white); font-size: 9.5px; font-weight: 300; line-height: 12px;
    margin-bottom: 6px; white-space: nowrap;
  }
  .contact__item--email { margin-top: 22px; }
  .contact__icon { width: 11px; height: 10px; flex: none; fill: var(--orange); }
</style>
</head>
<body>
<main class="canvas">
  <section class="card card--front" aria-label="Card front">
    <div class="card__stripe"></div>
    <div class="card__notch"></div>
    <div class="brand"><span class="brand__dot"></span><span class="brand__name">Harbourline<br>Pipeworks</span></div>
  </section>

  <section class="card card--back" aria-label="Card back">
    <div class="card__stripe"></div>
    <div class="card__notch"></div>
    <div class="brand"><span class="brand__dot"></span><span class="brand__name">Harbourline<br>Pipeworks</span></div>
    <div class="divider"></div>
    <div class="contact">
      <h1 class="contact__name">Warwick Tane</h1>
      <p class="contact__role">Director</p>
      <ul class="contact__list">
        <li class="contact__item">
          <svg class="contact__icon" viewBox="0 0 12 11" aria-hidden="true"><path d="M6 0 0 5h1.5v6h3.5V7.5h2V11h3.5V5H12z"/></svg>
          <span>PO Box 8716<br>Palmerston North 4441</span>
        </li>
        <li class="contact__item">
          <svg class="contact__icon" viewBox="0 0 12 11" aria-hidden="true"><path d="M1 2.5C1 1.5 2.5 0.5 6 0.5s5 1 5 2v1.5H8.5V3h-5v1H1zM2.5 5h7l1.5 5.5H1zM6 6a1.6 1.6 0 1 0 0 3.2A1.6 1.6 0 0 0 6 6z"/></svg>
          <span>027 815 0937</span>
        </li>
        <li class="contact__item contact__item--email">
          <svg class="contact__icon" viewBox="0 0 12 11" aria-hidden="true"><path d="M0 1.5h12v1L6 6 0 2.5zM0 4l6 3.5L12 4v6H0z"/></svg>
          <span>warwick@harbourlinepipeworks.example</span>
        </li>
      </ul>
    </div>
  </section>
</main>
</body>
</html>
```